Illustration of protein bar

we need protein bar illustration just like qto bar. Everything else will stay the same as mentioned in the image. All instructions are on attached image (sticker.jpg)

Please take our protein bar wrapper image (KRZFinalvector_noguides) and create a illustration just like sample bar image (qto bar). Our brand is crunvelle.

After the illustration of our protein bar is created please add the following around it as I mentioned in the Sticker image:

1. INTRODUCING NEW PROTEIN BAR
2. SOLD HERE with white arrow (i did a poor job drawing in photoshop)
3. "Crunvelle" logo information under the bar as mentioned in Sticker.jpg

The whole design will be used as poster or sticker therefore high res illustration file is needed. IF you have any questions please contact me contact@crunvelle-mail.com

I have attached PDF file as well or you can get all files from this link: https://www.dropvandle.com/download/QmRxT4p9LkWvZa7YhN2Cj
Updates

you can get all files from the following link

https://www.dropvandle.com/download/QmRxT4p9LkWvZa7YhN2Cj

Colors
f78f20
faa54b
fac995
9bcb3c
ec2027
0692cd

```html
<!DOCTYPE html>
<html lang="en">
<head>
<meta charset="utf-8">
<title>Crunvelle Mocha Peanut Crisp – Sold Here</title>
<link rel="stylesheet" href="https://fonts.googleapis.com/css2?family=Lobster+Two:ital,wght@1,700&family=Open+Sans:wght@600;700;800&display=swap">
<style>
  :root {
    --orange: #f78f20;
    --orange-mid: #faa54b;
    --orange-light: #fac995;
    --green: #9bcb3c;
    --red: #ec2027;
    --red-deep: #c1272d;
    --blue: #0692cd;
    --sky: #1fb1ea;
    --brown: #6b3a1e;
    --brown-dark: #4a2812;
    --white: #ffffff;
    --silver: #e6e8ea;
    --ink: #231f20;
  }
  html, body {
    margin: 0;
    padding: 0;
    width: 1200px;
    height: 900px;
    overflow: hidden;
    background: var(--white);
  }
  .poster {
    position: relative;
    width: 1200px;
    height: 900px;
    font-family: "Open Sans", Arial, sans-serif;
  }
  .poster-art {
    position: absolute;
    inset: 0;
    width: 1200px;
    height: 900px;
  }
  .script {
    font-family: "Lobster Two", cursive;
    font-style: italic;
    font-weight: 700;
  }
  .headline {
    font-size: 50px;
    fill: var(--white);
    stroke: #c8641a;
    stroke-width: 7px;
    paint-order: stroke;
    stroke-linejoin: round;
  }
  .tagline {
    font-size: 50px;
    fill: var(--red-deep);
    stroke: var(--white);
    stroke-width: 8px;
    paint-order: stroke;
    stroke-linejoin: round;
  }
  .sold-here {
    font-size: 56px;
    font-weight: 700;
    fill: var(--white);
  }
  .ribbon-small { font-size: 21px; font-weight: 800; fill: var(--white); }
  .ribbon-big { font-size: 48px; font-weight: 800; fill: var(--white); }
  .badge-label { font-size: 9px; font-weight: 700; fill: var(--ink); }
  .badge-value { font-size: 26px; font-weight: 700; fill: var(--ink); }
  .brand-name { font-size: 78px; font-weight: 800; fill: var(--red); }
  .flavour { font-size: 29px; font-weight: 800; fill: var(--brown); }
  .pack-tagline { font-size: 17px; font-weight: 700; fill: var(--orange); }
  .smart-choice { font-size: 19px; font-weight: 800; fill: var(--white); }
  .pack-note { font-size: 11px; font-weight: 700; fill: var(--ink); }
  .side-label { font-size: 12px; font-weight: 600; fill: var(--ink); }
  .side-value { font-size: 30px; font-weight: 700; fill: var(--ink); }
</style>
</head>
<body>
<main class="poster">
  <svg class="poster-art" viewBox="0 0 1200 900" xmlns="http://www.w3.org/2000/svg">
    <defs>
      <radialGradient id="burst" cx="0.5" cy="0.45" r="0.7">
        <stop offset="0" stop-color="#fff4e2"/>
        <stop offset="0.35" stop-color="var(--orange-light)"/>
        <stop offset="0.7" stop-color="var(--orange-mid)"/>
        <stop offset="1" stop-color="var(--orange)"/>
      </radialGradient>
      <linearGradient id="foil" x1="0" y1="0" x2="0" y2="1">
        <stop offset="0" stop-color="#d9dcdf"/>
        <stop offset="0.15" stop-color="var(--white)"/>
        <stop offset="0.8" stop-color="#f4f5f6"/>
        <stop offset="1" stop-color="#c9cdd1"/>
      </linearGradient>
      <linearGradient id="chocolate" x1="0" y1="0" x2="1" y2="1">
        <stop offset="0" stop-color="#5a3420"/>
        <stop offset="0.6" stop-color="#3e2214"/>
        <stop offset="1" stop-color="#2c170d"/>
      </linearGradient>
    </defs>

    <!-- background field -->
    <rect class="field" x="55" y="100" width="995" height="675" fill="url(#burst)"/>

    <!-- sold here band -->
    <g class="sold-band">
      <rect x="1048" y="100" width="102" height="675" fill="var(--red-deep)"/>
      <g class="sold-here" text-anchor="middle">
        <text x="1099" y="170">S</text>
        <text x="1099" y="228">O</text>
        <text x="1099" y="287">L</text>
        <text x="1099" y="345">D</text>
        <text x="1099" y="466">H</text>
        <text x="1099" y="524">E</text>
        <text x="1099" y="583">R</text>
        <text x="1099" y="641">E</text>
      </g>
      <path d="M1088 660 h22 v40 h18 l-29 52 l-29 -52 h18 z" fill="var(--white)"/>
    </g>

    <!-- headline -->
    <g class="script headline" text-anchor="middle">
      <text x="590" y="180">a perfect blend of crispy,</text>
      <text x="590" y="240">crunchy and chewy</text>
    </g>

    <!-- product pack -->
    <g class="pack" transform="rotate(-6 560 450)">
      <path class="pack-body" d="M120 300 L1000 300 L1000 610 L120 610 Z" fill="url(#foil)"/>
      <path class="pack-crimp-left" d="M108 300 h24 v310 h-24 z" fill="#dfe2e5"/>
      <path class="pack-crimp-right" d="M988 300 h24 v310 h-24 z" fill="#dfe2e5"/>
      <rect class="pack-stripe" x="120" y="300" width="880" height="4" fill="var(--red-deep)" opacity="0.6"/>

      <g class="pack-badge calories">
        <rect x="388" y="340" width="70" height="46" rx="6" fill="var(--sky)"/>
        <text class="badge-label" x="423" y="354" text-anchor="middle" textLength="62" lengthAdjust="spacingAndGlyphs">CALORIES ONLY</text>
        <text class="badge-value" x="423" y="380" text-anchor="middle">172</text>
      </g>
      <g class="pack-badge protein">
        <rect x="463" y="340" width="64" height="46" rx="6" fill="var(--orange)"/>
        <text class="badge-label" x="495" y="354" text-anchor="middle">PROTEIN</text>
        <text class="badge-value" x="495" y="380" text-anchor="middle">16g</text>
      </g>

      <circle class="brand-dot" cx="238" cy="410" r="11" fill="var(--red)"/>
      <text class="brand-name" x="225" y="475">crunvelle</text>
      <text class="flavour" x="290" y="507">Mocha Peanut Crisp</text>
      <text class="pack-tagline" x="290" y="532">nutritiously delicious protein bar</text>

      <rect class="smart-band" x="120" y="542" width="540" height="32" rx="10" fill="var(--green)"/>
      <text class="smart-choice" x="460" y="565">SMART CHOICE</text>

      <rect class="bar-photo" x="668" y="316" width="300" height="138" rx="14" fill="url(#chocolate)" role="img" aria-label="Photo of the mocha peanut crisp bar broken open, showing dark chocolate coating and peanuts"/>
      <text class="pack-note" x="818" y="478">REAL DARK</text>
      <text class="pack-note" x="818" y="492">CHOCOLATE</text>

      <circle cx="713" cy="540" r="7" fill="none" stroke="var(--ink)" stroke-width="1.5"/>
      <text class="pack-note" x="727" y="545">NET WT 1.59 OZ (45G)</text>
    </g>

    <!-- introducing ribbon -->
    <g class="ribbon" transform="rotate(-22 225 270)">
      <path d="M140 205 L315 205 L305 335 L245 320 L150 335 Z" fill="var(--red-deep)"/>
      <path d="M150 335 L170 360 L175 330 Z" fill="#8f1a1e"/>
      <g text-anchor="middle">
        <text class="ribbon-small" x="228" y="232">INTRODUCING</text>
        <text class="ribbon-big" x="228" y="280">NEW</text>
        <text class="ribbon-small" x="228" y="308">PROTEIN BAR</text>
      </g>
    </g>

    <!-- side facts -->
    <g class="fact protein">
      <rect x="873" y="592" width="97" height="70" rx="6" fill="var(--red-deep)"/>
      <text class="side-label" x="921" y="612" text-anchor="middle">PROTEIN</text>
      <text class="side-value" x="921" y="647" text-anchor="middle">16g</text>
    </g>
    <g class="fact calories">
      <rect x="875" y="672" width="97" height="72" rx="6" fill="var(--sky)"/>
      <text class="side-label" x="923" y="692" text-anchor="middle">CALORIES ONLY</text>
      <text class="side-value" x="923" y="728" text-anchor="middle">172</text>
    </g>

    <!-- tagline -->
    <text class="script tagline" x="525" y="722" text-anchor="middle">nutritiously delicious protein bar</text>
  </svg>
</main>
</body>
</html>
```